Web site design for Brivolt Software (www.brivoltsoftware-example.com)

Need the design as well as the html for the website. The brief is given in the attached file.
If possible, would like to use pencil sketches instead of images to give a unique look to the site.
Target Market(s)
small Software product companies
Industry/Entity Type
Software
Coding
Coded - Design and coding required
Number of Pages Required
5+ page

```html
<!DOCTYPE html>
<html lang="en">
<head>
<meta charset="utf-8">
<title>Brivolt Software</title>
<link href="https://fonts.googleapis.com/css2?family=Fira+Sans:wght@400;500&family=Fira+Mono&display=swap" rel="stylesheet">
<style>
:root{
  --page:#6a6a6a;
  --frame:#8a8a8a;
  --card:#6e6e6e;
  --ink:#1b1b1b;
  --ink-soft:#2a2a2a;
  --hero-text:#a3a3a3;
  --hero-a:#3a1215;
  --hero-b:#6e1a1f;
  --hero-c:#101418;
  --photo-grey:#8c8c8c;
  --photo-red:#6b1c1f;
  --label:#0d0d0d;
  --label-text:#bdbdbd;
  --panel-text:#b5b5b5;
}
*{margin:0;padding:0;box-sizing:border-box}
html,body{width:1200px;height:554px;overflow:hidden;background:var(--page)}
body{position:relative;font-family:"Fira Sans",Arial,sans-serif;color:var(--ink)}
.abs{position:absolute}
.brand{left:30px;top:16px;width:120px;height:14px;background:var(--label);color:var(--label-text);font:500 8px/14px "Fira Sans",sans-serif;letter-spacing:4px;padding-left:10px}
.menu{left:796px;top:16px;width:38px;height:14px;background:var(--label);color:var(--label-text);font:8px/14px "Fira Mono",monospace;text-align:center;letter-spacing:1px}
.frame{left:29px;top:30px;width:805px;height:496px;border:1px solid var(--frame);pointer-events:none}
.hero{left:29px;top:30px;width:493px;height:376px;background:radial-gradient(ellipse at 55% 20%,var(--hero-b),var(--hero-a) 45%,var(--hero-c) 90%)}
.hero h1{position:absolute;left:17px;top:232px;font:500 37px/37px "Fira Sans",sans-serif;color:var(--hero-text)}
.hero p{position:absolute;left:17px;top:314px;width:170px;font-size:7.5px;line-height:10px;color:var(--hero-text)}
.link{font:8px "Fira Mono",monospace;color:var(--ink-soft)}
.hero .link{position:absolute;left:17px;top:344px;color:var(--hero-text)}
.vision{left:523px;top:32px;width:309px;height:302px;background:linear-gradient(135deg,#9a9a9a,var(--photo-grey) 60%,#7d7d7d)}
.vision h2{position:absolute;left:11px;top:140px;font:500 20px/24.5px "Fira Sans",sans-serif;color:var(--ink)}
.vision p{position:absolute;left:11px;top:242px;width:270px;font-size:7.5px;line-height:10px}
.vision .link{position:absolute;left:11px;top:269px}
.card{top:406px;height:119px;background:var(--card);border-right:1px solid var(--frame)}
.card h3{position:absolute;left:17px;top:22px;font:500 13px "Fira Sans",sans-serif}
.card p{position:absolute;left:17px;top:44px;width:205px;font-size:7.5px;line-height:10px}
.card .link{position:absolute;left:17px;top:80px}
.card-a{left:29px;width:244px}
.card-b{left:273px;width:249px}
.video{left:525px;top:336px;width:133px;height:189px;background:linear-gradient(180deg,#262626 0%,#2e2e2e 40%,#3a3a3a 100%)}
.video .name{position:absolute;left:40px;top:30px;font-size:9px;color:var(--panel-text)}
.video .play{position:absolute;left:35px;top:125px;font:8px "Fira Mono",monospace;color:var(--panel-text)}
.red-photo{left:658px;top:336px;width:174px;height:106px;background:linear-gradient(120deg,#4a1214,var(--photo-red) 55%,#8a3a3a)}
.quote{left:658px;top:442px;width:174px;height:83px;background:var(--card)}
.quote p{position:absolute;left:19px;top:14px;width:150px;font-size:7.5px;line-height:10.5px}
.quote .author{position:absolute;left:19px;top:62px;font:7px "Fira Mono",monospace}
.quote .mark{position:absolute;right:6px;top:60px;font:500 22px "Fira Sans",sans-serif;color:#555}
.contact{left:847px;top:146px;width:200px;font-size:7px;line-height:9.6px;color:var(--ink)}
.contact .tag{display:inline-block;background:var(--label);color:var(--label-text);font:7.5px/11px "Fira Mono",monospace;padding:0 6px;letter-spacing:.5px;margin-bottom:6px}
.contact h4{font:400 7.8px "Fira Sans",sans-serif;margin-bottom:4px}
.contact .block{margin-bottom:8px}
.contact .tel{display:block;margin-top:3px}
.footer{left:28px;top:530px;font-size:6px;color:var(--ink-soft)}
.footer span{margin:0 3px}
</style>
</head>
<body>
<div class="abs brand">BRIVOLT</div>
<div class="abs menu">menu</div>

<section class="abs hero" role="img" aria-label="Abstract red perforated architectural facade">
  <h1>Driven by<br>architecture</h1>
  <p>Seasoned programmers who infuse rigor and design into solid engineering in software</p>
  <span class="link">&gt; who are we?</span>
</section>

<section class="abs vision" role="img" aria-label="Pencil-toned photo of an open hand">
  <h2>Creativity,<br>vision,<br>rigorousness,<br>and humanity</h2>
  <p>Over 10 software products for startups all over the world built to provide the best-in-class of UX, design rules and APIs.</p>
  <span class="link">&gt; expertise</span>
</section>

<section class="abs card card-a">
  <h3>Software implemented correctly</h3>
  <p>Learn how accomplish with our clients a happy collaboration where expectations of delivery and results are clear from the start.</p>
  <span class="link">&gt; engagement models</span>
</section>
<section class="abs card card-b">
  <h3>Giving back</h3>
  <p>We believe in giving back in our own small way. Over the years, we’ve been working hard to to put smiles on the faces of children across India.</p>
  <span class="link">&gt; partnership</span>
</section>

<section class="abs video" role="img" aria-label="Product graphic above a video still of a team member speaking">
  <span class="name">Nimbleware</span>
  <span class="play">&#9654; play video</span>
</section>

<div class="abs red-photo" role="img" aria-label="Red-toned portrait photo of a computing pioneer"></div>
<section class="abs quote">
  <p>"Progress is possible only if we train ourselves to think about programs without thinking of them as pieces of executable code."</p>
  <span class="author">Edwin V. Dorland</span>
  <span class="mark">”</span>
</section>

<div class="abs frame"></div>

<aside class="abs contact">
  <span class="tag">Contact info</span>
  <div class="block">
    <h4>Brivolt Software, Dublin</h4>
    Unit 4 Larchfield Court<br>Glenmarrow Road<br>Co.Carlow, Dublin<br>Ireland<span class="tel">t: +353 (0)86 5550142</span>
  </div>
  <div class="block">
    <h4>Brivolt Software, Pune</h4>
    Office 207, 42 Lake Street,<br>Kalvani Link Road,<br>Pune, 411099<br>India<span class="tel">t: +91 20 55500917</span>
  </div>
  <div class="block">
    <h4>Write to</h4>
    info@brivoltsoftware-example.com
  </div>
</aside>

<footer class="abs footer">© Brivolt Software 2017 —— <span>Terms of Us</span>|<span>Privacy Notice</span>|<span>Cookies Notice</span></footer>
</body>
</html>
```